Coming Soon page for a new fitness startup

We are a new startup based in Toronto, Canada working on a site and mobile app where people can register for athletic events such as running, cycling, triathlon, SUP, etc.

Participants will also be able to manage their clubs and team, and connect their fitness trackers so they have all their fitness data and friends in one place.

I like very simple designs and lots of whitespace. So no need for icons or unnecessary graphics.

I prefer having a mobile phone app instead of a hero image. No need to worry about the details within the mobile app for now, we can fill it in later. Here are some landing pages that I like.
https://pixelvault.example/torvanmelk/buckets/438197-Landing-Page

Attached is a wireframe that gives some sample content for each of the sections. Please do not take the wireframe too literally, it is only meant to illustrate the content that we are experimenting with and should give an idea of how much text will be on the page.

I have also attached the company logo files. The logo is not being used yet so feel free to simplify the logo if it doesn't look great with your design. For example, I'm ok with just the name "k7ravi" in white if that looks better.

Target Market(s)

Ages 25 to 45. Interested in running, cycling, triathlon, SUP, etc.

Industry/Entity Type

Fitness

Coding

Coded - Design and coding required

Number of Pages Required

1 page

Requirements
Should not have
• Any photos should not contain track and field events, or people in a gym. Any photos should have people running or cycling outdoors. I know that photos can be easily swapped out but it is distracting to review a design that has the wrong photos.

```html
<!DOCTYPE html>
<html lang="en">
<head>
<meta charset="utf-8">
<title>k7ravi – Coming Soon</title>
<link href="https://fonts.googleapis.com/css2?family=Poppins:ital,wght@0,300;0,400;0,500;0,600;1,400&display=swap" rel="stylesheet">
<style>
  :root {
    --red: #e3222f;
    --red-soft: #e04a52;
    --ink: #222;
    --body: #444;
    --muted: #666;
    --line: #cfcfcf;
    --panel: #f7f7f7;
    --white: #fff;
    --dark: #2b2b2b;
  }
  * { box-sizing: border-box; margin: 0; padding: 0; }
  html, body { width: 804px; height: 1200px; overflow: hidden; background: var(--white); }
  body { position: relative; font-family: "Poppins", sans-serif; color: var(--ink); }
  .abs { position: absolute; }

  .hero-bg { left: 0; top: 0; width: 804px; height: 460px; }
  .brand { left: 64px; top: 20px; display: flex; align-items: center; gap: 10px; }
  .brand-dot { width: 60px; height: 60px; border: 3px solid var(--white); border-radius: 50%; }
  .brand-name { color: var(--white); font-size: 32px; font-weight: 500; letter-spacing: .5px; }
  .menu { left: 720px; top: 39px; width: 18px; }
  .menu span { display: block; height: 3px; background: var(--white); margin-bottom: 3px; border-radius: 1px; }

  .phone { left: 96px; top: 152px; width: 164px; height: 360px; border-radius: 26px;
    background: linear-gradient(90deg, #e6e6e6, #fafafa 40%, #ececec); border: 1px solid #d6d6d6;
    box-shadow: 0 10px 20px rgba(0,0,0,.12); }
  .phone-cam { left: 80px; top: 16px; width: 5px; height: 5px; border-radius: 50%; background: #333; }
  .phone-speaker { left: 66px; top: 27px; width: 32px; height: 2px; background: #888; border-radius: 1px; }
  .phone-screen { left: 9px; top: 42px; width: 146px; height: 258px; background: var(--white); border: 1px solid #ccc; }
  .phone-home { left: 70px; top: 310px; width: 24px; height: 24px; border-radius: 6px; border: 1px solid #bbb; background: #f3f3f3; }
  .app-brand { left: 22px; top: 24px; display: flex; align-items: center; gap: 5px; }
  .app-brand .brand-dot { width: 36px; height: 36px; border: 2px solid var(--red); }
  .app-brand .brand-name { color: #333; font-size: 20px; }
  .app-art { left: 12px; top: 78px; width: 122px; height: 122px; border-radius: 50%;
    background: radial-gradient(circle, #555 0%, #2a2a2a 55%, rgba(255,255,255,0) 72%); }
  .app-dl { left: 59px; top: 222px; width: 28px; height: 28px; border-radius: 50%; border: 1.5px solid #555;
    display: flex; align-items: center; justify-content: center; }

  .hero-copy { left: 322px; top: 164px; width: 400px; color: var(--white); }
  .hero-title { font-size: 29px; font-weight: 600; line-height: 1.05; letter-spacing: .3px; }
  .hero-sub { font-size: 21px; font-weight: 600; margin-top: 2px; letter-spacing: .3px; }
  .hero-text { font-size: 10px; line-height: 16px; margin-top: 18px; width: 350px; font-weight: 300; }
  .hero-note { font-size: 10px; line-height: 16px; margin-top: 9px; width: 250px; font-weight: 300; }
  .notify { left: 321px; top: 339px; width: 334px; height: 31px; display: flex; }
  .notify-field { flex: 1; background: var(--white); display: flex; align-items: center; gap: 9px;
    padding-left: 10px; font-size: 8px; color: #333; }
  .notify-btn { width: 88px; background: var(--red); color: var(--white); font-size: 10px; font-weight: 600;
    display: flex; align-items: center; justify-content: center; letter-spacing: .3px; }
  .dots { left: 383px; top: 460px; display: flex; gap: 5px; align-items: center; }
  .dots span { width: 8px; height: 8px; border: 1px solid var(--red); border-radius: 50%; }
  .dots span.on { width: 11px; height: 11px; background: var(--red); }

  .intro { left: 0; top: 538px; width: 804px; text-align: center; }
  .intro h2 { font-size: 24px; font-weight: 500; letter-spacing: .3px; }
  .intro p { font-size: 11.5px; margin-top: 12px; color: #333; }

  .feature { top: 628px; width: 220px; display: flex; gap: 12px; }
  .feature-icon { flex: none; width: 58px; height: 58px; border-radius: 50%; border: 2px solid #444;
    border-right-color: transparent; display: flex; align-items: center; justify-content: center; transform: rotate(-20deg); }
  .feature-icon svg { transform: rotate(20deg); }
  .feature h3 { font-size: 14.5px; font-weight: 400; line-height: 18px; }
  .feature p { font-size: 8.3px; line-height: 15px; color: var(--body); margin-top: 8px; width: 140px; }

  .event { left: 0; top: 808px; width: 413px; height: 328px;
    background: linear-gradient(120deg, #e5555c, #d9404a 60%, #e36a6f); color: var(--white); }
  .event-copy { left: 66px; top: 76px; width: 330px; }
  .event h2 { font-size: 21px; font-weight: 400; }
  .event h3 { font-size: 15px; font-weight: 400; margin-top: 6px; }
  .event p { font-size: 10.5px; line-height: 17px; margin-top: 12px; }
  .event-btn { display: inline-block; margin-top: 16px; background: var(--dark); color: var(--white);
    font-size: 10.5px; padding: 5px 10px; border-radius: 2px; }

  .contact { left: 413px; top: 808px; width: 391px; height: 328px; background: var(--panel); }
  .contact h2 { position: absolute; left: 53px; top: 54px; font-size: 20px; font-weight: 400; color: #333; }
  .field { left: 53px; width: 265px; background: var(--white); border: 1px solid var(--line);
    font-size: 8px; font-style: italic; color: #555; padding: 9px 11px; }
  .send { left: 53px; top: 246px; width: 88px; height: 24px; background: var(--red); color: var(--white);
    font-size: 10px; font-weight: 500; display: flex; align-items: center; justify-content: center; border-radius: 2px; }

  .footer { left: 0; top: 1136px; width: 804px; height: 64px; }
  .footer-links { left: 66px; top: 25px; font-size: 8px; color: #333; }
  .footer-links span { margin: 0 6px; }
  .social { left: 366px; top: 22px; display: flex; gap: 3px; }
  .social span { width: 22px; height: 22px; border-radius: 50%; border: 1.5px solid #333; }
  .copyright { right: 66px; top: 25px; font-size: 8px; color: #333; }
</style>
</head>
<body>

  <svg class="abs hero-bg" viewBox="0 0 804 460" role="img" aria-label="Photo of a cyclist riding outdoors at dusk">
    <defs>
      <linearGradient id="heroShade" x1="0" y1="0" x2="1" y2="1">
        <stop offset="0" stop-color="#5a5550"/>
        <stop offset=".45" stop-color="#2f2e2c"/>
        <stop offset="1" stop-color="#1a1a19"/>
      </linearGradient>
    </defs>
    <polygon points="0,0 804,0 804,458 0,396" fill="url(#heroShade)"/>
  </svg>

  <div class="abs brand"><div class="brand-dot"></div><div class="brand-name">k7ravi</div></div>
  <div class="abs menu"><span></span><span></span><span></span></div>

  <div class="abs phone">
    <div class="abs phone-cam"></div>
    <div class="abs phone-speaker"></div>
    <div class="abs phone-screen">
      <div class="abs app-brand"><div class="brand-dot"></div><div class="brand-name">k7ravi</div></div>
      <div class="abs app-art" role="img" aria-label="Illustration of multisport athletes"></div>
      <div class="abs app-dl">
        <svg width="12" height="12" viewBox="0 0 12 12"><path d="M6 1v6M3 5l3 3 3-3M2 10h8" stroke="#e3222f" stroke-width="1.6" fill="none"/></svg>
      </div>
    </div>
    <div class="abs phone-home"></div>
  </div>

  <div class="abs hero-copy">
    <h1 class="hero-title">CONNECT YOUR TRAINING,</h1>
    <div class="hero-sub">Friends, &amp; Events In One Place</div>
    <p class="hero-text">Sed ut perspiciatis unde omnis iste natus error sit voluptatem accusantium doloremque laudantium, totam rem aperiam, eaque ipsa quae ab illo inventore veritatis et quasi architecto beatae</p>
    <p class="hero-note">Join our email list. A referral program is earning and you'll want to be the first to know.</p>
  </div>
  <div class="abs notify">
    <div class="notify-field">
      <svg width="10" height="8" viewBox="0 0 10 8"><rect x=".5" y=".5" width="9" height="7" fill="none" stroke="#333"/><path d="M.5.5l4.5 4 4.5-4" fill="none" stroke="#333"/></svg>
      email address
    </div>
    <div class="notify-btn">NOTIFY ME ›</div>
  </div>
  <div class="abs dots"><span class="on"></span><span></span><span></span></div>

  <section class="abs intro">
    <h2>Training And Racing All In One Place</h2>
    <p>A New Fitness Community Is Coming Soon.</p>
  </section>

  <div class="abs feature" style="left:66px">
    <div class="feature-icon">
      <svg width="26" height="26" viewBox="0 0 26 26"><rect x="2" y="4" width="22" height="20" rx="2" fill="none" stroke="#e3222f" stroke-width="2"/><path d="M2 10h22M7 1v6M19 1v6M8 14h2M12 14h2M16 14h2M8 18h2M12 18h2M16 18h2" stroke="#e3222f" stroke-width="2"/></svg>
    </div>
    <div><h3>Find<br>Events</h3><p>Sed ut perspiciatis unde omnis iste natus error sit voluptatem accusantium doloremque ntium, totam rem aperiam, eaque ipsa quae ab illo inventore</p></div>
  </div>
  <div class="abs feature" style="left:298px">
    <div class="feature-icon">
      <svg width="28" height="26" viewBox="0 0 28 26"><circle cx="8" cy="7" r="3" fill="none" stroke="#e3222f" stroke-width="1.6"/><circle cx="20" cy="7" r="3" fill="none" stroke="#e3222f" stroke-width="1.6"/><path d="M3 20v-5a5 5 0 0 1 10 0v5M15 20v-5a5 5 0 0 1 10 0v5M1 20h26" fill="none" stroke="#e3222f" stroke-width="1.6"/></svg>
    </div>
    <div><h3>Invite Your<br>Friends</h3><p>Sed ut perspiciatis unde omnis iste natus error sit voluptatem accusantium doloremque ntium, totam rem aperiam, eaque ipsa quae ab illo inventore</p></div>
  </div>
  <div class="abs feature" style="left:533px">
    <div class="feature-icon">
      <svg width="28" height="26" viewBox="0 0 28 26"><path d="M14 2L27 24H1z" fill="#e3222f"/><circle cx="14" cy="12" r="2" fill="#fff"/><circle cx="9" cy="19" r="2" fill="#fff"/><circle cx="19" cy="19" r="2" fill="#fff"/></svg>
    </div>
    <div><h3>Connect Your<br>Workouts</h3><p>Sed ut perspiciatis unde omnis iste natus error sit voluptatem accusantium doloremque ntium, totam rem aperiam, eaque ipsa quae ab illo inventore</p></div>
  </div>

  <section class="abs event" role="img" aria-label="Red-tinted photo of two runners training outdoors">
    <div class="abs event-copy">
      <h2>Organizing An Event?</h2>
      <h3>Attracting Participants Is Hand</h3>
      <p>With your event fisted on k7ravi well not not only handle the registration and payment process, we've also mode it our own personal mission to drive up participation numbers across all events.</p>
      <span class="event-btn">Contact us to learn more</span>
    </div>
  </section>

  <section class="abs contact">
    <h2>We'd Love To Hear From You</h2>
    <div class="abs field" style="top:95px;height:27px">Your Name</div>
    <div class="abs field" style="top:129px;height:26px">email address</div>
    <div class="abs field" style="top:162px;height:71px">How can we help?</div>
    <div class="abs send">SEND</div>
  </section>

  <footer class="abs footer">
    <div class="abs footer-links">About Us<span>|</span>Developers<span>|</span>Careers</div>
    <div class="abs social"><span></span><span></span><span></span></div>
    <div class="abs copyright">© Copyright 2018 k7ravi . All Rights Reserved.</div>
  </footer>

</body>
</html>
```